Property restoration company needs 'Appreciation Packet' to send customers

Need 3 items designed.
- a branded 'Thank You' greeting card. 4"x6" fold over style. Should look professional and match our brand identity. I would like to be able to get these printed with a specific message inside and also as blank-inside cards to hand write custom messages into.

Business is owned by a father and son. The thank you message in the card will be signed from both of us. I would like to add our pictures inside the card under the message to give it a personal feeling.

- a card requesting google reviews with a QR code linked to review form. Business card sized when printed. Front & Back printing.

- an information card explaining that we pay referral fees. Business card sized. Front & Back printing

```html
<!DOCTYPE html>
<html lang="en">
<head>
<meta charset="UTF-8">
<title>Thank You Card – Inside Spread</title>
<link rel="stylesheet" href="https://fonts.googleapis.com/css2?family=Arimo:wght@700&family=League+Spartan:wght@700&family=Allura&display=swap">
<style>
  :root {
    --backdrop: #e9edf2;
    --paper: #ffffff;
    --paper-shade: #f1f2f5;
    --fold-line: #dcdfe5;
    --brand-blue: #24559a;
    --photo-light: #8ea9cf;
    --photo-dark: #2b4f8a;
  }
  * { box-sizing: border-box; margin: 0; padding: 0; }
  html, body {
    width: 1200px;
    height: 799px;
    overflow: hidden;
    background: var(--backdrop);
  }
  .card-spread {
    position: absolute;
    left: 260px;
    top: 140px;
    width: 680px;
    height: 520px;
    display: flex;
    box-shadow: 0 6px 24px rgba(40, 60, 90, 0.18);
  }
  .card-panel {
    width: 340px;
    height: 520px;
    background: var(--paper);
  }
  .card-panel--blank {
    background: linear-gradient(90deg, var(--paper) 0%, var(--paper-shade) 100%);
    border-right: 1px solid var(--fold-line);
  }
  .card-panel--message {
    display: flex;
    flex-direction: column;
    align-items: center;
    padding: 44px 28px 0;
  }
  .message-title {
    font-family: "Arimo", Arial, sans-serif;
    font-weight: 700;
    font-size: 29px;
    line-height: 1.08;
    color: var(--brand-blue);
    text-align: center;
  }
  .message-body {
    margin-top: 16px;
    font-family: "League Spartan", sans-serif;
    font-weight: 700;
    font-size: 13.5px;
    line-height: 1.22;
    color: var(--brand-blue);
    text-align: center;
  }
  .owners-photo {
    margin-top: 26px;
    width: 262px;
    height: 196px;
  }
  .signatures {
    margin-top: 18px;
    width: 262px;
    display: flex;
    justify-content: space-around;
  }
  .signature {
    font-family: "Allura", cursive;
    font-size: 21px;
    color: var(--brand-blue);
  }
</style>
</head>
<body>
  <main class="card-spread">
    <section class="card-panel card-panel--blank" aria-label="Blank inside left panel"></section>
    <section class="card-panel card-panel--message">
      <h1 class="message-title">Thank you<br>for your order !</h1>
      <p class="message-body">
        We truly value your support and the<br>
        opportunity to serve you.<br>
        If you need any assistance, please<br>
        don’t hesitate to reach out.
      </p>
      <svg class="owners-photo" viewBox="0 0 262 196" role="img" aria-label="Photo of the two owners, father and son, in blue company shirts with arms crossed">
        <defs>
          <linearGradient id="ownersTone" x1="0" y1="0" x2="0" y2="1">
            <stop offset="0" stop-color="var(--photo-light)"/>
            <stop offset="1" stop-color="var(--photo-dark)"/>
          </linearGradient>
        </defs>
        <rect x="0" y="0" width="262" height="196" fill="url(#ownersTone)"/>
      </svg>
      <div class="signatures">
        <span class="signature">signacher</span>
        <span class="signature">signacher</span>
      </div>
    </section>
  </main>
</body>
</html>
```